Photographic Tutorial website

We are looking for a fresh design for a photographic tutorial / workshop website. The website will have the included functions:

* Home (needs to have a login section)
* About Us
* Info about each course / workshop.
* Subscribe to courses and pay online.
* Members Area
* Photo gallery
* Contact us

The website will be implemented with our own made cms. We do not need it to be coded. We have a team ready to do this for us. We only need the PSD layout.

We have attached a mockup design that the client and I have come up with and we need the design to be taken to the next level.

Client also likes:
http://www.vellowindstudio.example/

Photographic Interests

Online

Requirements
Must have
• Must Stand out i.e black backgrounds
Should not have
• Alter the logo in anyway.

```html
<!DOCTYPE html>
<html lang="en">
<head>
<meta charset="utf-8">
<title>Your Aperture Mate – Photographic Tuition</title>
<link href="https://fonts.googleapis.com/css2?family=Gelasio:ital,wght@0,400;0,700;1,400&family=Open+Sans:wght@400&display=swap" rel="stylesheet">
<style>
:root{
  --bg:#151515;
  --bg-header:#1b1b1b;
  --bg-footer:#1c1c1c;
  --text:#a9a9a9;
  --text-light:#dcdcdc;
  --heading:#cfcfcf;
  --accent:#d8222a;
  --accent-dim:#a8262b;
  --green:#3f9c3a;
  --rule:#2b2b2b;
  --serif:"Gelasio", Georgia, serif;
  --sans:"Open Sans", Arial, sans-serif;
}
*{margin:0;padding:0;box-sizing:border-box}
html,body{width:758px;height:1200px;overflow:hidden;background:var(--bg)}
body{position:relative;font-family:var(--serif);color:var(--text);font-size:11px}
.abs{position:absolute}
.site-header{left:0;top:0;width:758px;height:105px;background:linear-gradient(#232323,#171717)}
.brand{left:72px;top:52px;display:flex;align-items:center;gap:8px}
.brand-dot{width:26px;height:26px;border-radius:50%;background:#2a55b8}
.brand-name{font-size:24px;font-weight:700;color:var(--text-light);line-height:1}
.brand-tag{left:106px;top:76px;font-size:8px;letter-spacing:2px;color:var(--text-light)}
.main-nav{left:392px;top:76px;display:flex;gap:10px;font-size:11px;color:var(--text-light)}
.main-nav .current{border-bottom:2px solid #555;padding-bottom:3px}
.hero-band{left:0;top:105px;width:758px;height:280px;background:linear-gradient(90deg,#3a3a3a,#6a6a6a 50%,#3a3a3a)}
.hero-photo{left:63px;top:121px;width:634px;height:246px;border-radius:6px;border:1px solid #888;background:linear-gradient(180deg,#2f6a1e,#4d9a2a 40%,#2a4a18 75%,#8a7048)}
.slider-knob{left:358px;top:397px;width:44px;height:44px;border-radius:50%;background:radial-gradient(circle at 45% 40%,#f7a23a,#c25e06 55%,#3a2414 75%);box-shadow:0 0 14px #b55a10}
.thumb-rule{left:66px;width:632px;height:1px;background:var(--rule)}
.thumb{top:458px;width:72px;height:72px;border-radius:6px;border:1px solid #777}
.arrow{top:480px}
.heading{font-size:17px;color:var(--heading);font-weight:400}
.heading em{font-style:normal;color:var(--accent);font-weight:700}
.heading-rule{height:1px;background:var(--rule)}
.body-copy{font-size:11px;line-height:16px}
.schedule{left:65px;top:750px;width:392px;border-collapse:collapse;font-size:9.5px}
.schedule th{font-weight:400;text-decoration:underline;text-align:left;padding-bottom:8px;font-size:10px}
.schedule td{height:16px}
.schedule .c{text-align:center}.schedule .r{text-align:right}
.quote-by{color:var(--accent-dim);font-style:italic}
.member{left:492px;display:flex;gap:8px}
.member-photo{width:42px;height:43px;border:1px solid #777;background:linear-gradient(#6f7680,#2b2f36);flex:none}
.more-link{color:var(--accent-dim);font-style:italic;text-decoration:underline}
.footer-panel{left:0;top:940px;width:758px;height:190px;background:var(--bg-footer)}
.col-title{font-size:11px;color:var(--text-light);text-decoration:underline}
.col-title em{font-style:normal;color:var(--accent);font-weight:700}
.small{font-size:9.5px;line-height:16px}
.green{color:var(--green);font-style:italic;text-decoration:underline}
.map{left:275px;top:1017px;width:89px;height:91px;border:2px solid #ddd;background:linear-gradient(135deg,#c9d6df,#e8ece6 50%,#b6c8d6)}
.bottom-rule{left:66px;top:1131px;width:632px;height:1px;background:var(--rule)}
.copyright{left:70px;top:1152px;font-family:var(--sans);font-size:8px;color:var(--text-light)}
.social{top:1146px;width:18px;height:18px;border-radius:3px}
</style>
</head>
<body>
<header class="site-header abs"></header>
<div class="brand abs"><span class="brand-dot"></span><span class="brand-name">Your Aperture Mate</span></div>
<div class="brand-tag abs">PHOTOGRAPHIC TUITION</div>
<nav class="main-nav abs"><span class="current">Home</span><span>About Us</span><span>Our Courses</span><span>Members Area</span><span>Contact Us</span></nav>

<div class="hero-band abs"></div>
<div class="hero-photo abs" role="img" aria-label="Featured photo: tree-lined avenue in a green forest"></div>
<div class="slider-knob abs"></div>

<div class="thumb-rule abs" style="top:450px"></div>
<svg class="arrow abs" style="left:84px" width="16" height="30"><path d="M14 2 2 15l12 13" fill="none" stroke="#777" stroke-width="3"/></svg>
<div class="thumb abs" style="left:131px;background:linear-gradient(#3c7a22,#6b8a3a)" role="img" aria-label="Gallery thumbnail: forest avenue"></div>
<div class="thumb abs" style="left:216px;background:linear-gradient(#6f9bd0,#8a9aa6 60%,#4a6a2a)" role="img" aria-label="Gallery thumbnail: office tower"></div>
<div class="thumb abs" style="left:301px;background:linear-gradient(#0d1430,#1c2040 55%,#b8601c)" role="img" aria-label="Gallery thumbnail: city skyline at night"></div>
<div class="thumb abs" style="left:386px;background:linear-gradient(#3f86c9,#2d6aa8 55%,#1d3d66)" role="img" aria-label="Gallery thumbnail: lake view"></div>
<div class="thumb abs" style="left:471px;background:linear-gradient(#9bb6cf,#a8865a 50%,#4a6a32)" role="img" aria-label="Gallery thumbnail: historic building with fountain"></div>
<div class="thumb abs" style="left:556px;background:linear-gradient(#6f9bd0,#8a9aa6 60%,#4a6a2a)" role="img" aria-label="Gallery thumbnail: office tower"></div>
<svg class="arrow abs" style="left:659px" width="16" height="30"><path d="M2 2l12 13L2 28" fill="none" stroke="#777" stroke-width="3"/></svg>
<div class="thumb-rule abs" style="top:539px"></div>

<h2 class="heading abs" style="left:66px;top:564px"><em>Welcome</em> to our site</h2>
<div class="heading-rule abs" style="left:66px;top:592px;width:396px"></div>
<p class="body-copy abs" style="left:66px;top:600px;width:400px">The website will be implemented with our own made cms. We do not need it to be coded. We have a team ready to do this for us. We only need the PSD layout. The website will be implemented with our own made cms. We do not need it to be coded. We have a team ready to do this for us. We only need the PSD layout. The website will be implemented with our own made cms. We do not need it to be coded. We have a team ready to do this for us. We only need the PSD layout.</p>

<h2 class="heading abs" style="left:66px;top:710px"><em>Shooting</em> times</h2>
<div class="heading-rule abs" style="left:66px;top:738px;width:396px"></div>
<table class="schedule abs">
<tr><th>Day</th><th class="c">Subject</th><th class="r" style="text-align:right;padding-right:30px">Time</th></tr>
<tr><td>Monday</td><td class="c">Title Here</td><td class="r">10.00am - 12.00pm</td></tr>
<tr><td>Tuesday</td><td class="c">Title Here</td><td class="r">10.00am - 12.00pm</td></tr>
<tr><td>Wedday</td><td class="c">Title Here</td><td class="r">10.00am - 12.00pm</td></tr>
<tr><td>Thursday</td><td class="c">Title Here</td><td class="r">10.00am - 12.00pm</td></tr>
<tr><td>Friday</td><td class="c">Title Here</td><td class="r">10.00am - 12.00pm</td></tr>
<tr><td>Saturday</td><td class="c">Title Here</td><td class="r">10.00am - 11.00pm</td></tr>
</table>
<p class="abs small" style="left:66px;top:876px;width:395px"><span style="color:var(--text-light);font-weight:700;font-style:italic;text-decoration:underline">Nautical Twilight</span> start to end showes yoy the full information about our progarms. Nautical Twilight start to end showes yoy the full information about our progarms. Nautical Twilight start to end showes yoy the full information about our progarms.</p>

<h2 class="heading abs" style="left:493px;top:564px">Testimonials</h2>
<div class="heading-rule abs" style="left:493px;top:592px;width:203px"></div>
<p class="body-copy abs" style="left:493px;top:599px;width:200px"><span style="color:#555;font-size:16px">“</span> Your Aperture Mate photographic workshop have provided excellent trainning and I can now show off my pictures to my friends and family members. <span style="color:#555;font-size:16px">”</span></p>
<p class="quote-by abs" style="left:608px;top:678px">The Photographer</p>

<h2 class="heading abs" style="left:493px;top:710px"><em style="font-weight:400">Members</em> Gallery</h2>
<div class="heading-rule abs" style="left:493px;top:740px;width:203px"></div>
<div class="member abs" style="top:749px"><div class="member-photo" role="img" aria-label="Member portrait"></div><p class="body-copy" style="width:150px">Some text goes here to explain members speech about this workshop or courses.</p></div>
<div class="member abs" style="top:802px"><div class="member-photo" role="img" aria-label="Member portrait"></div><p class="body-copy" style="width:150px">Some text goes here to explain members speech about this workshop or courses.</p></div>
<div class="member abs" style="top:855px"><div class="member-photo" role="img" aria-label="Member portrait"></div><p class="body-copy" style="width:150px">Some text goes here to explain members speech about this workshop or courses.</p></div>
<a class="more-link abs" style="left:638px;top:912px">Know More</a>

<div class="footer-panel abs"></div>
<h3 class="col-title abs" style="left:66px;top:955px;font-weight:400"><em>Photographer's</em> Checklist</h3>
<ol class="small abs" style="left:66px;top:981px;list-style:none">
<li>1. Wedding shot checklist.</li><li>2. Pre-shoot checklist.</li><li>3. Standard checklist.</li>
<li class="green" style="margin-top:2px">Links &amp; reviews</li>
<li style="margin-top:4px">Headline goes here. Headline goes here.</li>
<li style="margin-top:4px">Headline goes here. Headline goes here</li>
<li style="margin-top:4px">Headline goes here. Headline goes here</li>
</ol>
<div class="abs" style="left:261px;top:955px;width:1px;height:160px;background:var(--rule)"></div>
<h3 class="col-title abs" style="left:274px;top:955px;font-weight:400"><em>General</em> Information &amp; <em>YAM's</em> 2012</h3>
<p class="small abs" style="left:274px;top:978px;width:215px">Some text goes here to explain your details matter. Some text goes here to explain your details matter.</p>
<div class="map abs" role="img" aria-label="Map of the workshop locations"></div>
<p class="small abs" style="left:376px;top:1014px;width:112px"><span class="green">Moon phase Chart</span><br>Some text goes here, put some text here. Some text goes here, put some text here. Some text goes here, put some text here.</p>
<div class="abs" style="left:501px;top:955px;width:1px;height:160px;background:var(--rule)"></div>
<h3 class="col-title abs" style="left:514px;top:955px;font-weight:400"><em>Our</em> Blogs</h3>
<div class="small abs" style="left:515px;top:978px;width:180px">
<p style="color:var(--text-light);font-style:italic;text-decoration:underline">Photography Blog</p>
<p class="green">Main Topic</p>
<p>Some text goes here, put some text here.</p>
<p>Dt : 12-02-2012</p>
<p style="color:var(--text-light);font-style:italic;text-decoration:underline;margin-top:6px">USA Full Tour &amp; Travel Blog</p>
<p class="green">Main Topic</p>
<p>Some text goes here, put some text here.</p>
<p>Dt : 02-05-2012</p>
</div>
<a class="more-link abs" style="left:638px;top:1108px">Know More</a>

<div class="bottom-rule abs"></div>
<p class="copyright abs">© 2012 Copyright &nbsp; | &nbsp; Your Aperture Mate &nbsp; | &nbsp; Developed by, <span style="font-style:italic;text-decoration:underline">HarbourWebWorks</span></p>
<p class="abs" style="left:570px;top:1150px;font-size:10px">Find Us &nbsp;|</p>
<div class="social abs" style="left:616px;background:#3fa0d8" aria-label="Follow link"></div>
<div class="social abs" style="left:644px;background:#3b5998" aria-label="Follow link"></div>
<div class="social abs" style="left:673px;background:#1a7ab3" aria-label="Follow link"></div>
</body>
</html>
```